Banner Design for High End Jewelry Website

We need a banner for our website (brivela.com) for a sale that we will be running. The banner should be a size 1187 × 400. I have included a few pieces of jewelry to be included in the banner (do not need to use all, can use just some). The banner should say:
"Christmas is Closer Than You Think Sale!"
Shop Now

Industry/Entity Type

Jewelry

```html
<!DOCTYPE html>
<html lang="en">
<head>
<meta charset="utf-8">
<title>Brivela Christmas Sale Banner</title>
<link rel="stylesheet" href="https://fonts.googleapis.com/css2?family=Jost:wght@400;600&display=swap">
<style>
  :root {
    --page-bg: #ffffff;
    --banner-edge: #d9bfa6;
    --banner-glow: #fbf7f1;
    --banner-mid: #eadccb;
    --ink-brown: #8a7266;
    --button-fill: #8f7668;
    --button-ink: #ffffff;
    --gold: #d8b24a;
    --gold-deep: #b9892a;
    --ruby: #a2203e;
    --emerald: #2f8a52;
    --setting-dark: #4e4a42;
  }
  html, body {
    margin: 0;
    padding: 0;
    width: 1200px;
    height: 1200px;
    overflow: hidden;
    background: var(--page-bg);
  }
  .canvas {
    position: relative;
    width: 1200px;
    height: 1200px;
  }
  .sale-banner {
    position: absolute;
    left: 74px;
    top: 405px;
    width: 1052px;
    height: 354px;
    overflow: hidden;
    background:
      radial-gradient(ellipse 46% 62% at 50% 52%, var(--banner-glow) 0%, rgba(251,247,241,0.85) 45%, rgba(251,247,241,0) 100%),
      linear-gradient(180deg, var(--banner-edge) 0%, var(--banner-mid) 45%, #f3ebe2 75%, #ecdccd 100%);
  }
  .product {
    position: absolute;
  }
  .product--earrings {
    left: 38px;
    top: 105px;
    width: 238px;
    height: 154px;
    border-radius: 40px;
    background: radial-gradient(ellipse at 50% 50%, var(--ruby) 0%, var(--gold) 35%, var(--gold-deep) 70%, rgba(216,178,74,0) 100%);
  }
  .product--brooch {
    left: 780px;
    top: 83px;
    width: 238px;
    height: 198px;
    border-radius: 50%;
    background: radial-gradient(circle at 50% 50%, var(--ruby) 0%, var(--gold) 28%, var(--gold-deep) 70%, var(--setting-dark) 100%);
  }
  .headline {
    position: absolute;
    left: 304px;
    top: 128px;
    width: 460px;
    margin: 0;
    font-family: "Jost", sans-serif;
    font-weight: 400;
    font-size: 42px;
    line-height: 58px;
    color: var(--ink-brown);
    text-align: center;
    letter-spacing: -0.3px;
  }
  .headline strong {
    font-weight: 600;
  }
  .shop-button {
    position: absolute;
    left: 414px;
    top: 263px;
    width: 222px;
    height: 50px;
    background: var(--button-fill);
    color: var(--button-ink);
    font-family: "Jost", sans-serif;
    font-weight: 400;
    font-size: 27px;
    line-height: 50px;
    text-align: center;
    text-decoration: none;
    letter-spacing: 0.5px;
  }
</style>
</head>
<body>
<div class="canvas">
  <section class="sale-banner">
    <div class="product product--earrings" role="img" aria-label="Pair of gold figure-eight earrings set with emerald and ruby cabochons and diamonds"></div>
    <h1 class="headline"><strong>Christmas</strong> is Closer<br>Thank You Think <strong>Sale!</strong></h1>
    <a class="shop-button" href="#">SHOP NOW</a>
    <div class="product product--brooch" role="img" aria-label="Gold floral brooch with a central ruby cabochon and diamond accents"></div>
  </section>
</div>
</body>
</html>
```